Velmont Recycling needs a new web design

We need a new web design for our company based in Austin, TX. We resell and recycling electronics such as laptops, computer components, Zelvos, Quorbs, etc. Since our inception over ten years ago, we’ve become one of the premier electronics recycling and remarketing companies in Austin, Texas.

```html
<!DOCTYPE html>
<html lang="en">
<head>
<meta charset="utf-8">
<title>Velmont Recycling</title>
<link href="https://fonts.googleapis.com/css2?family=Poppins:wght@500;600;700&family=Rubik:wght@400;500&display=swap" rel="stylesheet">
<style>
:root{
  --blue:#1a6bc1;
  --blue-deep:#155aa6;
  --navy:#0d1c2b;
  --black:#111;
  --green:#5cbf3a;
  --ink:#222;
  --muted:#555;
  --grey-bg:#eef0f4;
  --white:#fff;
}
*{margin:0;padding:0;box-sizing:border-box}
html,body{width:1200px;height:3340px;overflow:hidden}
body{position:relative;font-family:"Rubik",sans-serif;color:var(--ink);background:var(--white)}
.abs{position:absolute}
h2,h3,.brand{font-family:"Poppins",sans-serif}
.accent{color:var(--blue)}
.btn{position:absolute;display:flex;align-items:center;justify-content:center;border-radius:20px;font:500 12px "Rubik",sans-serif;color:var(--white);background:var(--blue)}
/* header */
.site-header{top:0;left:0;width:1200px;height:82px;background:var(--white)}
.brand{display:flex;align-items:center;gap:10px;font-weight:700;font-size:22px;color:var(--navy)}
.brand-dot{width:34px;height:34px;border-radius:50%;border:3px solid var(--blue)}
.phone{left:700px;top:28px;font:600 19px "Poppins",sans-serif;color:var(--navy);display:flex;gap:8px;align-items:center}
.nav{top:82px;left:0;width:1200px;height:38px;background:var(--navy)}
.nav ul{list-style:none;position:absolute;left:212px;top:0;display:flex;height:38px}
.nav li{font:500 11px "Rubik",sans-serif;color:var(--white);padding:0 18px;line-height:38px}
.nav li.active{background:var(--blue)}
.search{left:835px;top:8px;width:153px;height:23px;border-radius:12px;background:var(--white);font-size:10px;color:#999;padding:5px 12px}
/* hero */
.hero{top:120px;left:0;width:1200px;height:477px;background:linear-gradient(180deg,#6fa6e0 0%,#bcd8f0 45%,#9cc84a 62%,#4f8d1f 100%)}
.hero h1{position:absolute;left:209px;top:140px;font:700 28px/40px "Poppins",sans-serif;color:var(--navy)}
.hero p{position:absolute;left:209px;top:192px;width:470px;font-size:15px;line-height:22px;color:#1e2b38}
.arrow{width:36px;height:36px;border-radius:50%;background:#333;top:200px}
/* products */
.section-title{position:absolute;width:1200px;text-align:center;font:600 25px "Poppins",sans-serif;color:var(--black)}
.blob{position:absolute;width:118px;height:112px;border-radius:55% 45% 50% 50% / 60% 55% 45% 40%;display:flex;flex-direction:column;align-items:center;justify-content:center;gap:8px;color:var(--white);font-size:11px}
.blob.blue{background:var(--blue)}.blob.black{background:var(--black)}.blob.green{background:var(--green)}
.product-art{left:490px;top:735px;width:222px;height:378px;border-radius:20px;background:radial-gradient(circle at 50% 60%,#5cbf3a 0%,#9aa6b0 45%,#e8ebee 100%)}
/* about */
.about{top:1042px;left:0;width:1200px;height:472px;background:var(--grey-bg)}
.about-art{left:211px;top:128px;width:323px;height:255px;border-radius:50%;background:radial-gradient(circle,#b9c2c8 0%,#6cae3c 55%,#eef0f4 75%)}
.about h2{position:absolute;left:612px;top:150px;font-size:27px;line-height:38px;font-weight:600}
.about p{position:absolute;left:612px;width:430px;font-size:13px;line-height:21px;color:var(--muted)}
/* panels */
.panel{top:1514px;width:600px;height:400px;color:var(--white);text-align:center}
.panel small{display:block;margin-top:80px;font-size:13px}
.panel h3{font-size:28px;line-height:40px;font-weight:600;margin-top:4px}
.panel p{width:400px;margin:14px auto 0;font-size:12.5px;line-height:20px}
.panel .btn{left:225px;top:292px;width:150px;height:32px;background:var(--white);color:var(--ink)}
/* computer */
.made-easy h2{position:absolute;left:209px;top:1972px;font-size:28px;line-height:34px;font-weight:600}
.made-easy p{position:absolute;left:209px;width:370px;font-size:13px;line-height:21px;color:var(--muted)}
.video{left:590px;top:1990px;width:398px;height:252px;background:linear-gradient(135deg,#3a4f3a,#1d2620 60%,#5f6b66)}
/* certified */
.certified{top:2326px;left:0;width:1200px;height:568px;background:#f1f2f4}
.cert{position:absolute;top:178px;width:191px;height:267px;border:3px solid #222;background:linear-gradient(180deg,#e6efe2,#cfe0c8)}
/* footer */
.footer{top:2894px;left:0;width:1200px;height:446px;background:var(--blue)}
.footer .label{position:absolute;left:209px;font-size:11px;color:#cfe0f4;letter-spacing:.5px}
.footer .val{position:absolute;left:209px;font:500 14px "Rubik",sans-serif;color:var(--white);line-height:21px}
.social{position:absolute;top:326px;width:20px;height:20px;background:var(--white);border-radius:2px}
.contact{left:588px;top:2840px;width:380px;height:410px;background:var(--white);box-shadow:0 2px 14px rgba(0,0,0,.12)}
.contact h2{text-align:center;margin-top:18px;font-size:25px;line-height:36px;font-weight:600}
.contact p{width:344px;margin:8px auto 0;text-align:center;font-size:11.5px;line-height:18px}
.field{position:absolute;height:32px;border:1px solid #ddd;font-size:11px;color:#999;padding:9px 8px}
.copyright{position:absolute;top:3290px;width:1200px;text-align:center;font-size:11px;color:#dbe8f6}
</style>
</head>
<body>
<header class="site-header abs">
  <div class="brand abs" style="left:212px;top:22px"><span class="brand-dot"></span>VELMONT</div>
  <div class="phone abs"><svg width="18" height="18" viewBox="0 0 24 24"><path d="M6.6 10.8a15 15 0 0 0 6.6 6.6l2.2-2.2a1 1 0 0 1 1-.25 11 11 0 0 0 3.6.6 1 1 0 0 1 1 1V20a1 1 0 0 1-1 1A17 17 0 0 1 3 4a1 1 0 0 1 1-1h3.5a1 1 0 0 1 1 1c0 1.25.2 2.450.6 3.6a1 1 0 0 1-.25 1z" fill="#1a6bc1"/></svg>(512) 555-0147</div>
  <div class="btn" style="left:884px;top:27px;width:104px;height:31px">Book Online</div>
</header>
<nav class="nav abs">
  <ul><li class="active">HOME</li><li>ABOUT</li><li>SERVICES</li><li>CERTIFICATIONS</li><li>NEWS</li><li>CONTACT</li></ul>
  <div class="search abs">Search</div>
</nav>

<section class="hero abs" role="img" aria-label="Sunny sky over green grass with a recycling bin full of electronics">
  <h1><span class="accent">Recycling Today</span> Reuse Tomorrow</h1>
  <p>We resell and recycling electronics such as laptops, computer components, Zelvos, Quorbs, etc.</p>
  <div class="btn" style="left:209px;top:256px;width:150px;height:34px">Schedule &amp; Pickup</div>
  <div class="btn" style="left:366px;top:256px;width:150px;height:34px;background:var(--black)">Call (512) 555-0147</div>
  <div class="arrow abs" style="left:77px"><svg width="36" height="36"><path d="M21 11l-7 7 7 7" stroke="#fff" stroke-width="2.5" fill="none"/></svg></div>
  <div class="arrow abs" style="left:1085px"><svg width="36" height="36"><path d="M15 11l7 7-7 7" stroke="#fff" stroke-width="2.5" fill="none"/></svg></div>
</section>

<h2 class="section-title" style="top:652px"><span class="accent">Recycling</span> Products</h2>
<div class="product-art abs" role="img" aria-label="Recycling bin full of electronics"></div>
<div class="blob blue" style="left:211px;top:757px"><svg width="32" height="26"><rect x="2" y="2" width="28" height="17" rx="2" fill="none" stroke="#fff" stroke-width="2"/><path d="M10 24h12M16 19v5" stroke="#fff" stroke-width="2"/></svg>Computers</div>
<div class="blob black" style="left:350px;top:757px"><svg width="34" height="26"><rect x="6" y="3" width="22" height="15" rx="1" fill="none" stroke="#fff" stroke-width="2"/><path d="M2 22h30" stroke="#fff" stroke-width="2"/></svg>Laptops</div>
<div class="blob green" style="left:305px;top:880px"><svg width="24" height="30"><rect x="5" y="2" width="14" height="26" rx="2" fill="none" stroke="#fff" stroke-width="2"/></svg>Email Devices</div>
<div class="blob black" style="left:737px;top:757px"><svg width="32" height="26"><rect x="2" y="2" width="28" height="17" rx="2" fill="none" stroke="#fff" stroke-width="2"/><path d="M10 24h12" stroke="#fff" stroke-width="2"/></svg>Quorbs</div>
<div class="blob blue" style="left:875px;top:757px"><svg width="30" height="30"><rect x="4" y="4" width="22" height="22" rx="3" fill="none" stroke="#fff" stroke-width="2"/><rect x="10" y="10" width="10" height="10" fill="#fff"/></svg>Components</div>
<div class="blob green" style="left:828px;top:880px"><svg width="26" height="32"><rect x="3" y="2" width="20" height="28" rx="3" fill="none" stroke="#fff" stroke-width="2"/></svg>Zelvos</div>

<section class="about abs">
  <div class="about-art abs" role="img" aria-label="Grass recycling arrows circling a bin of electronics"></div>
  <h2><span class="accent">About</span> Velmont Recycling</h2>
  <p style="top:200px">At Velmont Recycling, we're committed to providing environmentally friendly recycling solutions to Austin and the surrounding areas.</p>
  <p style="top:258px">Founded in 2006, our mission is to process your materials in a safe, non-hazardous manner – with an aim to keep the world environmentally clean. As a R2 recycling center, we believe in promoting smart recycling habits in order to achieve long lasting results.</p>
  <div class="btn" style="left:612px;top:362px;width:148px;height:30px">Schedule &amp; Pickup</div>
</section>

<section class="panel abs" style="left:0;background:linear-gradient(rgba(21,90,166,.88),rgba(21,90,166,.88)),#0b2f5a" role="img" aria-label="Blue tinted photo of recycling bins">
  <small>Environmentally Friendly</small>
  <h3>Electronic Recycling</h3>
  <p>At Velmont Recycling, we strive to keep the environment clean through our wide range of services. Our E-Waste Recycling services were designed to simplify the recycling process for residents in the Austin area. Contact us today and see how you can contribute to making this world a cleaner place.</p>
  <div class="btn">Schedule &amp; Pickup</div>
</section>
<section class="panel abs" style="left:600px;background:linear-gradient(rgba(20,20,20,.85),rgba(20,20,20,.85)),#444" role="img" aria-label="Dark tinted photo of a pickup crew loading electronics">
  <small>We Come To You</small>
  <h3>Recycling Pickup</h3>
  <p>At Velmont Recycling, we go out of our way to make sure your recycling process is made easy as possible. Our Recycling Pickup service is designed to simplify all of your recycling needs . Take a look at all the services we offer and get in touch to see how you can start the process today!</p>
  <div class="btn">Schedule &amp; Pickup</div>
</section>

<section class="made-easy">
  <h2><span class="accent">Computer Recycling</span><br>Made Easy</h2>
  <p style="top:2050px">Want to make a difference to our environment and planet? Velmont Recycling is here to help! Velmont recycling has been helping keep the environment healthy since 2006.</p>
  <p style="top:2132px">we specialize in recycling services that help citizens become experts at reducing waste. We have a passion to keep our world clean and are here to guide you through all the stages of the recycling process.</p>
  <div class="btn" style="left:209px;top:2236px;width:108px;height:32px">Read More</div>
  <div class="abs" style="left:570px;top:1977px;width:30px;height:30px;border-left:12px solid var(--blue);border-top:12px solid var(--blue)"></div>
  <div class="abs" style="left:958px;top:2230px;width:30px;height:30px;border-right:12px solid var(--blue);border-bottom:12px solid var(--blue)"></div>
  <div class="video abs" role="img" aria-label="Video still of a hand touching recycle icons">
    <svg class="abs" style="left:169px;top:96px" width="60" height="60"><circle cx="30" cy="30" r="27" fill="none" stroke="#fff" stroke-width="3"/><path d="M24 18l16 12-16 12z" fill="#fff"/></svg>
  </div>
</section>

<section class="certified abs">
  <h2 class="section-title" style="top:58px"><span class="accent">Certified</span> Recyclers</h2>
  <p class="abs" style="left:290px;top:116px;width:620px;text-align:center;font-size:12px;line-height:19px;color:var(--muted)">Processing of electronic assets and electronic scrap, all associated site operations and maintenance, as well as the supporting financial and administrative functions related to these activities and operations.</p>
  <div class="cert" style="left:209px;background:var(--blue);color:#fff;text-align:center;font-size:11.5px;line-height:18px;padding:40px 12px 0">Has been assessed by Norland Registrar and found to be in compliance with the following Environmental Management Standard: ISO 14001:2015
    <div class="btn" style="left:45px;top:196px;width:95px;height:32px;background:#fff;color:var(--ink)">Full View</div>
  </div>
  <div class="cert" style="left:407px" role="img" aria-label="Certificate of certification"></div>
  <div class="cert" style="left:603px" role="img" aria-label="Certificate of certification"></div>
  <div class="cert" style="left:799px;background:#fafafa" role="img" aria-label="State environmental registration letter"></div>
</section>

<footer class="footer abs">
  <div class="brand abs" style="left:209px;top:60px;color:#fff"><span class="brand-dot" style="border-color:#fff"></span>VELMONT</div>
  <div class="label" style="top:133px">ADDRESS</div>
  <div class="val" style="top:148px">4120 Larkspur Ave<br>Austin TX USA 78745</div>
  <div class="label" style="top:209px">PHONE</div>
  <div class="val" style="top:224px">(512) 555-0147</div>
  <div class="label" style="top:265px">EMAIL</div>
  <div class="val" style="top:280px">jen@velmontrecycling.com</div>
  <div class="social" style="left:209px"></div>
  <div class="social" style="left:235px"></div>
  <div class="social" style="left:261px"></div>
</footer>
<section class="contact abs">
  <h2><span class="accent">Contact</span> Us</h2>
  <p>Interested in helping to make the world a greener place? Get in touch with Velmont Recycling, and learn more about the wide range of recycling services and facilities that are at your disposal.</p>
  <div class="field" style="left:22px;top:150px;width:165px;border-color:var(--blue)">Name</div>
  <div class="field" style="left:193px;top:150px;width:165px">Email</div>
  <div class="field" style="left:22px;top:188px;width:165px">Phone</div>
  <div class="field" style="left:193px;top:188px;width:165px">Subject</div>
  <div class="field" style="left:22px;top:226px;width:336px">Address</div>
  <div class="field" style="left:22px;top:264px;width:336px;height:80px">Message</div>
  <div class="btn" style="left:22px;top:356px;width:336px;height:32px;border-radius:0">SEND MESSAGE</div>
</section>
<div class="copyright">©2019 by Velmont Recycling. All Rights Reserved</div>
</body>
</html>
```